The Bramblewood Roadside Defense Guide
An Owner's Notes on Quietly Settling Every Old Dispute
The Bramblewood Roadside Defense Guide - Law
This book will be read by middle class, well educated people with pending reckless driving charges.
Dimensions are approximately 6.5" x 8.5" (half sheet). We would like the title, sub title and the author's name ( Owen T. Marsh) to appear on the front cover. No text on the spine (about 1/8" spine). The back page will have no text. but the design on the back cover should allow us to place a text layer on top of the back cover design - so the back cover design should not make it difficult to read the text. (See attached example from previous project)
omarsh omarsh
#99 #100 #101 Submissions should not have any text on the back cover. Please remove the text from the back cover if you want your submission to be considered.
#61 - Can you do some variations of the text. Perhaps tweak the color or the color gradient.
#36 #66 #61 #45 #42 #53 #45 These are the top contenders. These are all awesome designs! To be selected the design must include back and front covers and NOT contain "2nd edition"
#36 #66 #61 #45 To be considered you must have a back cover as well as a front cover. Please resubmit your design with a back cover
#61 Can you take off the "2nd edition" from the front - this is not the second edition.
#14 my wife likes this one so that is a plus.:)
#7 this looks like a book on Velvet Harbor - Awesome! but probably not a great angle for a law firm :) I wonder if they would sue me if we just put a crystal pyramid and rainbow on the cover?
#11 nice design but too similar to the DUI book cover.
#14 Reckless driving cases are 80% speed related so the cover matches the subject well and it breaks away from the frame clip art pack nicely. The is something about it that says "Car ad" rather than legal book though. Maybe its the bright colors and contemporary "smart car" looking vehicle. May be look for different versions of the same theme and see.
#23 - forgot the title.
#20 I like the dirty scratched texture you did in #8 better, it makes it seem more interesting. #8's texturing is pretty heavy though, a slightly toned version, something in between #8 and #20 might be a good idea, no 100% sure though. I still think there needs to be some original graphic on the cover instead of just the text or framed clip art.
#9 I like that you are creating original images instead of just using the clip art whole-cloth and getting rid of the borders. That doesn't mean that a submission couldn't have a square frame clip art, it just means that originality scores points.
#22 Not bad, but the simplicity takes away from the professionalism. The look is not bad but then you realize its just swirled sirens with the clip art pasted on top. If the cover image was something original or it used some original elements in it I think it would help overcome that. I really like that your submissions are all over the place and not just a different versions of the same thing.
#19 I like that concept of this design. Its abstract, not just clip art photography pastes on the cover. Its completely unique from the other too examples of book covers. The colors and text are not my favorite. So the execution is not there yet but the fact that it is completely going off on its own is a big plus.
#8 I like the design of the scratched surface and the yellow hash marks...but it seems a little off. I don't know that the clip art I uploaded really matches. I can't help but wonder if something with traffic cones or a speed limit sign might be better. Don't know for sure...just vague impressions.
#21 this looks too similar to what we already have and is not very contemporary. Keep trying though.
#18 is a bit too similar to the DUI book cover I uploaded as an example. I don't want to be derivative.
#1 I think the police tap doesn't really match the Reckless driving. Most reckless driving cases are for speeding or minor car accidents, falling asleep at the wheel or someone doing doughnuts in a parking lot. Police crime scene tape doesn't usually come into play.
#2,#,3,#4 I marked these low because this is a reckless driving book not DUI. Reckless driving is not generally an alcohol offense in Va and so the covers' designs were a bit confusing.

```html
<!DOCTYPE html>
<html lang="en">
<head>
<meta charset="utf-8">
<title>The Bramblewood Roadside Defense Guide — Cover Spread</title>
<link rel="stylesheet" href="https://fonts.googleapis.com/css2?family=Archivo+Black&family=Arimo:wght@400;700&display=swap">
<style>
  :root {
    --paper: #ffffff;
    --back-red: #8c0b0b;
    --cover-yellow: #f1c81e;
    --spine-blue: #2a3a8c;
    --title-red: #c8141b;
    --ink: #111111;
    --photo-dark: #0d1630;
    --photo-mid: #3a3f6e;
    --photo-red: #b0222c;
  }
  html, body {
    margin: 0;
    padding: 0;
    width: 1200px;
    height: 790px;
    overflow: hidden;
    background: var(--paper);
  }
  .spread {
    position: relative;
    width: 1200px;
    height: 790px;
    background: var(--paper);
  }
  .back-cover {
    position: absolute;
    left: 14px;
    top: 19px;
    width: 580px;
    height: 754px;
    background: var(--back-red);
  }
  .front-cover {
    position: absolute;
    left: 604px;
    top: 19px;
    width: 584px;
    height: 754px;
    background: var(--cover-yellow);
    overflow: hidden;
  }
  .spine-band {
    position: absolute;
    left: 0;
    top: 0;
    width: 9px;
    height: 100%;
    background: var(--spine-blue);
  }
  .title-block {
    position: absolute;
    left: 9px;
    right: 0;
    top: 22px;
    text-align: center;
  }
  .title-lead,
  .title-tail {
    font-family: "Arimo", Arial, sans-serif;
    font-weight: 700;
    color: var(--title-red);
    line-height: 1;
    margin: 0;
  }
  .title-lead {
    font-size: 38px;
    padding-left: 110px;
    text-align: left;
  }
  .title-main {
    font-family: "Archivo Black", "Arial Black", sans-serif;
    font-size: 84px;
    color: var(--ink);
    line-height: 1;
    margin: 4px 0 0;
    letter-spacing: -1px;
  }
  .title-tail {
    font-size: 44px;
    margin-top: 4px;
  }
  .subtitle {
    font-family: "Arimo", Arial, sans-serif;
    font-weight: 700;
    font-size: 19px;
    line-height: 1.2;
    text-transform: uppercase;
    color: var(--ink);
    margin: 14px 0 0;
    letter-spacing: 0.3px;
  }
  .cover-photo {
    position: absolute;
    left: 9px;
    right: 0;
    top: 283px;
    height: 376px;
    background:
      radial-gradient(ellipse at 30% 20%, rgba(255,80,90,0.55), transparent 45%),
      radial-gradient(ellipse at 80% 35%, rgba(90,120,255,0.45), transparent 40%),
      linear-gradient(180deg, var(--photo-mid) 0%, var(--photo-dark) 55%, #1b1b2a 100%);
  }
  .author {
    position: absolute;
    left: 9px;
    right: 0;
    bottom: 28px;
    text-align: center;
    font-family: "Arimo", Arial, sans-serif;
    font-weight: 700;
    font-size: 40px;
    color: var(--ink);
    margin: 0;
  }
</style>
</head>
<body>
  <main class="spread">
    <section class="back-cover" aria-label="Back cover"></section>
    <section class="front-cover" aria-label="Front cover">
      <div class="spine-band"></div>
      <header class="title-block">
        <h1>
          <span class="title-lead" style="display:block">The Bramblewood</span>
          <span class="title-main" style="display:block">Roadside</span>
          <span class="title-tail" style="display:block">Defense Guide</span>
        </h1>
        <p class="subtitle">An Owner's Notes on Quietly<br>Settling Every Old Dispute</p>
      </header>
      <div class="cover-photo" role="img" aria-label="Night photo of police cruisers with flashing red and blue lights on a city street"></div>
      <p class="author">Owen T. Marsh</p>
    </section>
  </main>
</body>
</html>
```